Soap/cosmetic labels

Need labels that incorporate my brand , to fit onto rectangular and round labels readable down to two inches. Key ideas are luxury, nourishing, handmade, palm oil/paraben free, cruelty free, savon artisanal. One line will be called The Gentle Cake by The Meadow Wren with key words: fragrance free, all natural colorants. The other line is luxury oils, fragrance, indulgent and just The Meadow Wren

Target Market(s)

Women mostly

Industry/Entity Type

cosmetics/soap

Colors
0094D4
00A9DD
6FCCEA
C7EBF8
E9F6FB

Requirements
Must have
• place for me to change fragrance and cosmetic type; gold goes on black labels; blue on white labels
Nice to have
• fit the brand

```html
<!DOCTYPE html>
<html lang="en">
<head>
<meta charset="utf-8">
<title>The Gentle Cake – Label Set</title>
<link rel="stylesheet" href="https://fonts.googleapis.com/css2?family=Marcellus&family=Allura&family=Fira+Sans+Condensed:wght@500&display=swap">
<style>
  :root {
    --canvas: #ffffff;
    --label-dark: #2b2b2d;
    --label-dark-edge: #232325;
    --label-light: #f3f3f3;
    --gold: #d6b35e;
    --gold-band: #d9b863;
    --blue: #0094d4;
    --blue-bright: #00a9dd;
    --blue-band: #2fb1e2;
    --ink-light: #ececec;
    --ink-dark: #4a4a4a;
    --ink-band: #2a2a2a;
  }
  * { margin: 0; padding: 0; box-sizing: border-box; }
  html, body {
    width: 1200px; height: 1200px; overflow: hidden;
    background: var(--canvas);
  }
  .label-set {
    position: relative; width: 1200px; height: 1200px;
    display: flex; justify-content: center; align-items: center; gap: 60px;
  }
  .label {
    position: relative; width: 420px; height: 760px;
    border-radius: 18px; overflow: hidden;
    display: flex; flex-direction: column; align-items: center;
  }
  .label--black {
    background: linear-gradient(160deg, var(--label-dark) 0%, var(--label-dark-edge) 100%);
    --accent: var(--gold);
    --copy: var(--ink-light);
    --band: var(--gold-band);
  }
  .label--white {
    background: var(--label-light);
    --accent: var(--blue-bright);
    --copy: var(--ink-dark);
    --band: var(--blue-band);
  }
  .brand-mark {
    width: 150px; height: 150px; border-radius: 50%;
    background: var(--accent);
    margin-top: 68px;
  }
  .brand-name {
    margin-top: 34px;
    font-family: "Marcellus", serif;
    font-size: 38px; line-height: 1;
    color: var(--accent);
    letter-spacing: 0.5px;
    white-space: nowrap;
  }
  .product {
    margin-top: 108px;
    width: 320px;
    position: relative;
  }
  .product-name {
    font-family: "Allura", cursive;
    font-size: 60px; line-height: 1;
    color: var(--accent);
    text-align: center;
    white-space: nowrap;
  }
  .product-by {
    font-family: "Marcellus", serif;
    font-size: 14px; letter-spacing: 1px;
    color: var(--copy);
    margin-top: 2px; margin-left: 4px;
  }
  .claims {
    margin-top: 64px;
    font-family: "Fira Sans Condensed", sans-serif;
    font-weight: 500;
    font-size: 21px; letter-spacing: 1.6px;
    line-height: 36px;
    color: var(--copy);
    text-align: center;
  }
  .volume-band {
    position: absolute; left: 0; right: 0; bottom: 0;
    height: 82px;
    background: var(--band);
    display: flex; align-items: center; justify-content: center;
    font-family: "Fira Sans Condensed", sans-serif;
    font-weight: 500;
    font-size: 21px; letter-spacing: 1.6px;
    color: var(--ink-band);
  }
</style>
</head>
<body>
  <main class="label-set">
    <section class="label label--black">
      <div class="brand-mark" aria-hidden="true"></div>
      <h1 class="brand-name">The Meadow Wren</h1>
      <div class="product">
        <h2 class="product-name">The Gentle Cake</h2>
        <p class="product-by">BY THE MEADOW WREN</p>
      </div>
      <p class="claims">FRAGRANCE FREE<br>ALL NATURAL COLORANTS</p>
      <div class="volume-band">500 ML</div>
    </section>

    <section class="label label--white">
      <div class="brand-mark" aria-hidden="true"></div>
      <h1 class="brand-name">The Meadow Wren</h1>
      <div class="product">
        <h2 class="product-name">The Gentle Cake</h2>
        <p class="product-by">BY THE MEADOW WREN</p>
      </div>
      <p class="claims">FRAGRANCE FREE<br>ALL NATURAL COLORANTS</p>
      <div class="volume-band">500 ML</div>
    </section>
  </main>
</body>
</html>
```